Brell Harbor Company Business Cards

Front and Back Business Card - logo and text setup - cool design. I need workable photoshop or illustrator files so I can setup each employee card with design that is created
Updates

Hi everyone, thank you for the great entries. Please no more white and blue cards - there are so many already - black and silver only now please. thanks!

Target Market(s)

Construction Industry - Facility Managers

Industry/Entity Type

Construction

Contact Information for Business Card

I really like contemporary simplistic looks - clean neat....not opposed to seeing some black backrounds

Requirements
Must have
• Logo/website address with design on front only - www.brellharbor-example.com (logo attached)
• Back:
• Name/Title/Company Address/Phone/email address
Nice to have
• Cool design
Should not have
• Nothing gimmicky like Fire or Water - since we are a Fire Protection company - it has all been done

```html
<!DOCTYPE html>
<html lang="en">
<head>
<meta charset="utf-8">
<title>Brell Harbor Company – Business Cards</title>
<link href="https://fonts.googleapis.com/css2?family=Questrial&display=swap" rel="stylesheet">
<style>
  :root {
    --backdrop: #e4e4e6;
    --silver-light: #eceded;
    --silver: #b9bcc0;
    --silver-dark: #8c9096;
    --black: #141414;
    --charcoal: #2a2b2d;
  }
  * { margin: 0; padding: 0; box-sizing: border-box; }
  html, body {
    width: 1200px;
    height: 462px;
    overflow: hidden;
    background: var(--backdrop);
  }
  .sheet {
    position: relative;
    width: 1200px;
    height: 462px;
    font-family: "Questrial", "Century Gothic", sans-serif;
  }
  .card {
    position: absolute;
    top: 79px;
    width: 525px;
    height: 309px;
    overflow: hidden;
  }
  .card--contact { left: 57px; background: var(--silver-light); }
  .card--brand { left: 625px; background: var(--black); }

  .card__bands {
    position: absolute;
    inset: 0;
    width: 525px;
    height: 309px;
  }
  .band--silver { fill: var(--silver); }
  .band--black { fill: var(--black); }
  .band--rule { fill: var(--silver-dark); }

  .company-name {
    position: absolute;
    white-space: nowrap;
    font-weight: 400;
  }
  .card--contact .company-name {
    left: 21px;
    top: 22px;
    font-size: 30px;
    color: var(--black);
    letter-spacing: 0.5px;
  }
  .person {
    position: absolute;
    left: 22px;
    top: 68px;
    color: var(--charcoal);
  }
  .person__name {
    font-size: 17px;
    letter-spacing: 2px;
  }
  .person__title {
    margin-top: 4px;
    font-size: 13px;
    letter-spacing: 2.4px;
    color: var(--silver-dark);
  }

  .contact-list {
    position: absolute;
    left: 16px;
    top: 187px;
    list-style: none;
  }
  .contact-list__item {
    display: flex;
    align-items: center;
    height: 27px;
    color: var(--silver-light);
    font-size: 14.5px;
    letter-spacing: 2.8px;
  }
  .contact-list__icon {
    width: 15px;
    height: 15px;
    margin-right: 14px;
    flex: none;
  }
  .contact-list__icon .solid { fill: var(--silver); }
  .contact-list__icon .line { fill: none; stroke: var(--silver); stroke-width: 1.6; }

  .card--brand .company-name {
    left: 0;
    right: 0;
    top: 112px;
    text-align: center;
    font-size: 42px;
    color: var(--silver-light);
    letter-spacing: 0.5px;
  }
  .brand-rule {
    position: absolute;
    left: 172px;
    width: 181px;
    top: 180px;
    height: 2px;
    background: var(--silver-dark);
  }
  .brand-web {
    position: absolute;
    left: 0;
    right: 0;
    top: 230px;
    text-align: center;
    color: var(--silver);
    font-size: 18px;
    letter-spacing: 3.5px;
  }
</style>
</head>
<body>
<main class="sheet">

  <section class="card card--contact" aria-label="Card front with contact details">
    <svg class="card__bands" viewBox="0 0 525 309" aria-hidden="true">
      <polygon class="band--silver" points="0,140 525,124 525,309 0,309"/>
      <polygon class="band--black" points="0,150 525,176 525,309 0,309"/>
      <polygon class="band--rule" points="0,148 525,174 525,177 0,151"/>
    </svg>

    <p class="company-name">Brell Harbor Company</p>
    <div class="person">
      <p class="person__name">Your Name</p>
      <p class="person__title">Your Title</p>
    </div>

    <ul class="contact-list">
      <li class="contact-list__item">
        <svg class="contact-list__icon" viewBox="0 0 16 16" aria-hidden="true">
          <path class="solid" d="M8,0.8 C4.9,0.8 2.6,3.1 2.6,6.1 C2.6,10 8,15.4 8,15.4 C8,15.4 13.4,10 13.4,6.1 C13.4,3.1 11.1,0.8 8,0.8 Z M8,8.2 A2.1,2.1 0 1 1 8,4 A2.1,2.1 0 1 1 8,8.2 Z"/>
        </svg>
        Your Adrress Here
      </li>
      <li class="contact-list__item">
        <svg class="contact-list__icon" viewBox="0 0 16 16" aria-hidden="true">
          <path class="solid" d="M3.4,1.2 L5.8,1.2 L6.8,4.6 L5.2,5.8 C6,7.8 8.2,10 10.2,10.8 L11.4,9.2 L14.8,10.2 L14.8,12.6 C14.8,13.8 13.8,14.8 12.6,14.8 C6.6,14.6 1.4,9.4 1.2,3.4 C1.2,2.2 2.2,1.2 3.4,1.2 Z"/>
          <path class="line" d="M9.2,1.6 A5.4,5.4 0 0 1 14.4,6.8 M9,4 A3,3 0 0 1 12,7"/>
        </svg>
        Your Phone Number
      </li>
      <li class="contact-list__item">
        <svg class="contact-list__icon" viewBox="0 0 16 16" aria-hidden="true">
          <rect class="line" x="1" y="3.2" width="14" height="9.6"/>
          <path class="line" d="M1,3.2 L8,9 L15,3.2"/>
        </svg>
        name@email.com
      </li>
      <li class="contact-list__item">
        <svg class="contact-list__icon" viewBox="0 0 16 16" aria-hidden="true">
          <circle class="line" cx="8" cy="8" r="6.8"/>
          <path class="line" d="M1.2,8 L14.8,8 M8,1.2 C4.6,4.6 4.6,11.4 8,14.8 M8,1.2 C11.4,4.6 11.4,11.4 8,14.8"/>
        </svg>
        www.brellharbor-example.com
      </li>
    </ul>
  </section>

  <section class="card card--brand" aria-label="Card back with company name">
    <p class="company-name">Brell Harbor Company</p>
    <div class="brand-rule" aria-hidden="true"></div>
    <p class="brand-web">www.brellharbor-example.com</p>
  </section>

</main>
</body>
</html>
```